Norvane Builders Business Card

Modern and Professional Business Card for a Med size construction/development company.

See the samples below for the design I like … but I need ideas for incorporating the red company logo while still keeping the clean look of the card samples that are attached.

Logo and tag line on the back … info on the front.

Tagline: Quality Starts from the Ground Up

Target Market(s)

Med-Large General Contractors

Contact Information for Business Card

Norvane Builders Limited
42 Brenton Street
Elk Harbour, NL
B3K 7T2

t: 709-555-0147
f: 709-555-0192
w: www.norvanebuilders-example.com

Font styles to use
Sans Serif

Colors
fbee3e

Requirements
Must have
• I like the black and yellow designs of the attached samples …. but I'm not sure how to incorporate the red Norvane Builders logo into that design??
Nice to have
• Construction safety strips

```html
<!DOCTYPE html>
<html lang="en">
<head>
<meta charset="utf-8">
<title>Norvane Builders Business Card</title>
<link rel="stylesheet" href="https://fonts.googleapis.com/css2?family=Open+Sans:wght@600;700;800&display=swap">
<style>
  :root {
    --safety-yellow: #fbee3e;
    --card-black: #1c1c1c;
    --ink: #111111;
    --paper-white: #ffffff;
    --backdrop: #2b2d30;
  }
  * { margin: 0; padding: 0; box-sizing: border-box; }
  html, body {
    width: 1200px;
    height: 900px;
    overflow: hidden;
    background: var(--backdrop);
    font-family: "Open Sans", sans-serif;
  }
  .canvas {
    position: relative;
    width: 1200px;
    height: 900px;
  }
  .card {
    position: absolute;
    left: 250px;
    width: 700px;
    height: 400px;
    overflow: hidden;
  }

  /* Back: brand side */
  .card-back {
    top: 40px;
    background: var(--safety-yellow);
    color: var(--ink);
    display: flex;
    flex-direction: column;
    align-items: center;
    justify-content: center;
    text-align: center;
  }
  .brand-name {
    font-weight: 800;
    font-size: 62px;
    line-height: 1;
    letter-spacing: 1px;
    text-transform: uppercase;
  }
  .brand-suffix {
    margin-top: 10px;
    font-weight: 800;
    font-size: 30px;
    letter-spacing: 3px;
    text-transform: uppercase;
  }
  .tagline {
    margin-top: 22px;
    font-weight: 700;
    font-size: 17px;
    letter-spacing: 2px;
    text-transform: uppercase;
  }

  /* Front: contact side */
  .card-front {
    top: 460px;
    background: var(--card-black);
    color: var(--paper-white);
  }
  .front-brand {
    position: absolute;
    left: 40px;
    top: 0;
    width: 270px;
    height: 100%;
    display: flex;
    flex-direction: column;
    justify-content: center;
    font-weight: 800;
    text-transform: uppercase;
    line-height: 1.05;
  }
  .front-brand .name { font-size: 40px; }
  .front-brand .suffix { font-size: 20px; letter-spacing: 2px; margin-top: 6px; }
  .contact-band {
    position: absolute;
    left: 330px;
    top: 0;
    width: 64px;
    height: 100%;
    background: var(--safety-yellow);
  }
  .contact-list {
    position: absolute;
    left: 330px;
    top: 0;
    height: 100%;
    display: flex;
    flex-direction: column;
    justify-content: center;
    gap: 22px;
    list-style: none;
  }
  .contact-item {
    display: flex;
    align-items: center;
  }
  .contact-icon {
    width: 64px;
    display: flex;
    justify-content: center;
    flex-shrink: 0;
  }
  .contact-icon svg { width: 22px; height: 22px; fill: var(--ink); }
  .contact-text {
    margin-left: 26px;
    font-weight: 600;
    font-size: 21px;
    line-height: 1.3;
  }
</style>
</head>
<body>
<main class="canvas">

  <section class="card card-back" aria-label="Card back">
    <div class="brand-name">Norvane Builders</div>
    <div class="brand-suffix">Limited</div>
    <p class="tagline">Quality Starts from the Ground Up</p>
  </section>

  <section class="card card-front" aria-label="Card front">
    <div class="front-brand">
      <span class="name">Norvane<br>Builders</span>
      <span class="suffix">Limited</span>
    </div>
    <div class="contact-band"></div>
    <ul class="contact-list">
      <li class="contact-item">
        <span class="contact-icon">
          <svg viewBox="0 0 24 24" aria-hidden="true"><path d="M12 2a7 7 0 0 0-7 7c0 5 7 13 7 13s7-8 7-13a7 7 0 0 0-7-7zm0 9.5A2.5 2.5 0 1 1 12 6.5a2.5 2.5 0 0 1 0 5z"/></svg>
        </span>
        <span class="contact-text">42 Brenton Street<br>Elk Harbour, NL B3K 7T2</span>
      </li>
      <li class="contact-item">
        <span class="contact-icon">
          <svg viewBox="0 0 24 24" aria-hidden="true"><path d="M6.6 10.8a15 15 0 0 0 6.6 6.6l2.2-2.2a1 1 0 0 1 1-.25 11.4 11.4 0 0 0 3.6.57 1 1 0 0 1 1 1V20a1 1 0 0 1-1 1A17 17 0 0 1 3 4a1 1 0 0 1 1-1h3.5a1 1 0 0 1 1 1c0 1.25.2 2.45.57 3.6a1 1 0 0 1-.25 1z"/></svg>
        </span>
        <span class="contact-text">709-555-0147</span>
      </li>
      <li class="contact-item">
        <span class="contact-icon">
          <svg viewBox="0 0 24 24" aria-hidden="true"><path d="M7 2h8l3 3v5H7zM4 11h16a2 2 0 0 1 2 2v7a2 2 0 0 1-2 2H4a2 2 0 0 1-2-2v-7a2 2 0 0 1 2-2zm2 3v2h5v-2zm9 0v2h3v-2zm0 3v2h3v-2z"/></svg>
        </span>
        <span class="contact-text">709-555-0192</span>
      </li>
      <li class="contact-item">
        <span class="contact-icon">
          <svg viewBox="0 0 24 24" aria-hidden="true"><path d="M12 2a10 10 0 1 0 0 20 10 10 0 0 0 0-20zm6.9 9h-3a15 15 0 0 0-1.3-5.6A8 8 0 0 1 18.9 11zM12 4c.9 1.2 1.8 3.6 1.9 7h-3.8c.1-3.4 1-5.8 1.9-7zM9.4 5.4A15 15 0 0 0 8.1 11h-3a8 8 0 0 1 4.3-5.6zM5.1 13h3a15 15 0 0 0 1.3 5.6A8 8 0 0 1 5.1 13zM12 20c-.9-1.2-1.8-3.6-1.9-7h3.8c-.1 3.4-1 5.8-1.9 7zm2.6-1.4a15 15 0 0 0 1.3-5.6h3a8 8 0 0 1-4.3 5.6z"/></svg>
        </span>
        <span class="contact-text">www.norvanebuilders-example.com</span>
      </li>
    </ul>
  </section>

</main>
</body>
</html>
```